Solar Company Solution Brochures

We are looking for a brochure design and theme that we can use moving forward. We are a solar microgrid company in New Zealand. We sell solar solutions and want a brochure for our most common solution. I have many other images and information so do ask. Solution diagram is shown and parts involved are also included. I dont want pricing on brochure.
Further work will be available to winner.

Target Market(s)

Offgrid solar customers.

Industry/Entity Type

Solar Energy

```html
<!DOCTYPE html>
<html lang="en">
<head>
<meta charset="utf-8">
<title>Kauri Grid Solar – Off Grid Brochure</title>
<link rel="stylesheet" href="https://fonts.googleapis.com/css2?family=Montserrat:wght@400;600;700;800&family=Open+Sans:wght@400;600&display=swap">
<style>
  :root{
    --ink:#2b2d31;
    --ink-deep:#1f2024;
    --green:#7cc242;
    --green-dark:#5fa32d;
    --paper:#ffffff;
    --page-bg:#e9eaec;
    --muted:#6b6e74;
    --line:#d5d7da;
    --sky:#9dc3dd;
    --sky-deep:#4f7fa3;
    --panel-blue:#2f3f5c;
  }
  *{box-sizing:border-box;margin:0;padding:0}
  html,body{width:795px;height:1200px;overflow:hidden}
  body{background:var(--page-bg);font-family:"Open Sans",Arial,sans-serif;color:var(--ink);position:relative}
  .spread{position:absolute;left:20px;width:755px;height:534px;display:flex;box-shadow:0 6px 18px rgba(0,0,0,.18)}
  .spread--outside{top:40px}
  .spread--inside{top:626px}
  .page{position:relative;width:50%;height:100%;background:var(--paper);overflow:hidden}
  .h{font-family:"Montserrat",Arial,sans-serif;font-weight:800;text-transform:uppercase;letter-spacing:.02em}
  .photo{position:absolute}
  .brand{font-family:"Montserrat",Arial,sans-serif;font-weight:700;color:var(--ink);display:flex;align-items:center;gap:6px;letter-spacing:.04em}
  .brand__square{width:10px;height:10px;background:var(--green)}

  /* back cover */
  .back__photo{left:0;top:0;width:190px;height:210px;background:linear-gradient(160deg,#b9d3e6 0%,#7fa6c4 45%,#3c5a7a 100%)}
  .back__text{position:absolute;left:205px;top:24px;width:155px}
  .back__text h3{font-size:10px;line-height:1.25;margin-bottom:6px}
  .back__text p{font-size:7px;line-height:1.5;color:var(--muted);margin-bottom:14px}
  .back__brand{position:absolute;left:205px;top:250px;font-size:17px}
  .back__contact{position:absolute;left:0;right:0;top:330px;height:30px;background:var(--green);display:flex;align-items:center;padding-left:28px}
  .back__contact span{color:#fff;font-size:12px}
  .back__details{position:absolute;left:28px;top:378px;font-size:8px;line-height:2.1;color:var(--ink)}
  .back__details div{display:flex;align-items:center;gap:7px}
  .back__details svg{width:10px;height:10px;fill:var(--green-dark)}
  .back__foot{position:absolute;left:0;right:0;bottom:0;height:34px;background:var(--ink)}

  /* front cover */
  .front__photo{left:0;top:0;width:100%;height:300px;background:linear-gradient(180deg,var(--sky) 0%,#d9e6ee 45%,#8f98a3 100%)}
  .front__logo{position:absolute;right:0;top:22px;width:170px;height:52px;background:var(--ink-deep);display:flex;align-items:center;justify-content:center}
  .front__logo .brand{color:#fff;font-size:15px}
  .front__shapes{position:absolute;left:0;top:230px;width:100%;height:140px}
  .front__title{position:absolute;left:60px;right:0;top:278px;height:112px;background:var(--ink);padding:20px 22px 0 26px}
  .front__title h1{color:#fff;font-size:19px;line-height:1.25}
  .front__bottom{position:absolute;left:0;right:0;bottom:26px;display:flex;justify-content:space-between;padding:0 26px;font-size:8px;color:var(--ink)}
  .front__bottom div{display:flex;align-items:center;gap:6px}
  .front__bottom svg{width:10px;height:10px;fill:var(--green-dark)}

  /* inside */
  .band{position:absolute;left:18px;right:18px;height:20px;background:var(--ink);color:#fff;font-size:9px;display:flex;align-items:center;justify-content:center;border-bottom:3px solid var(--green)}
  .product-grid{position:absolute;left:18px;right:18px;top:50px;display:grid;grid-template-columns:repeat(4,1fr);gap:8px}
  .product{display:flex;flex-direction:column;align-items:center;gap:4px}
  .product__img{width:100%;height:92px;background:linear-gradient(180deg,#f1f2f4,#c9ccd1)}
  .product__img--panel{background:linear-gradient(160deg,#3b4c6b,#1e2a40)}
  .product__label{font-size:7px;font-weight:600;color:var(--ink)}
  .features{position:absolute;left:18px;right:18px;display:grid;grid-template-columns:repeat(2,1fr);gap:10px}
  .feature{border:1px solid var(--line)}
  .feature__title{background:var(--green);color:#fff;font-family:"Montserrat",Arial,sans-serif;font-weight:700;font-size:8px;padding:4px 8px;text-transform:uppercase}
  .feature__text{font-size:7px;color:var(--muted);padding:6px 8px 8px;line-height:1.45}
  .right__products{position:absolute;left:18px;right:18px;top:50px;display:grid;grid-template-columns:repeat(3,1fr);gap:8px}
  .right__products .product__img{height:78px}
  .right__features{position:absolute;left:18px;right:18px;top:168px;display:grid;grid-template-columns:repeat(3,1fr);gap:8px}
  .install__photo{left:18px;right:18px;top:260px;height:256px;background:linear-gradient(180deg,#a9c9df 0%,#e7eef2 40%,#6d7f94 62%,#9a8a6a 100%)}
</style>
</head>
<body>

<section class="spread spread--outside" aria-label="Brochure outside spread">
  <article class="page page--back">
    <div class="photo back__photo" role="img" aria-label="Photo of two installers beside a solar panel array"></div>
    <div class="back__text">
      <h3 class="h">The passion behind the Kauri Grid solution</h3>
      <p>Built in Northland for homes beyond the grid, our systems deliver clean, reliable power every day.</p>
      <h3 class="h">The panel and trained installers</h3>
      <p>Certified local installers design, fit and support every system we supply.</p>
    </div>
    <div class="brand back__brand"><span class="brand__square"></span>KAURI GRID SOLAR</div>
    <div class="back__contact"><span class="h">Contact us</span></div>
    <div class="back__details">
      <div><svg viewBox="0 0 24 24"><path d="M12 2a7 7 0 0 0-7 7c0 5 7 13 7 13s7-8 7-13a7 7 0 0 0-7-7zm0 9.5A2.5 2.5 0 1 1 12 6.5a2.5 2.5 0 0 1 0 5z"/></svg>12 Harbour Road, Whangārei 0110</div>
      <div><svg viewBox="0 0 24 24"><path d="M6.6 10.8a15 15 0 0 0 6.6 6.6l2.2-2.2a1 1 0 0 1 1-.25 11.4 11.4 0 0 0 3.6.57 1 1 0 0 1 1 1V20a1 1 0 0 1-1 1A17 17 0 0 1 3 4a1 1 0 0 1 1-1h3.5a1 1 0 0 1 1 1c0 1.25.2 2.45.57 3.57a1 1 0 0 1-.25 1z"/></svg>0800 528 474</div>
      <div><svg viewBox="0 0 24 24"><path d="M3 5h18v14H3zm2 2v.5l7 4.5 7-4.5V7z"/></svg>hello@kaurigridsolar.co.nz</div>
    </div>
    <div class="back__foot"></div>
  </article>

  <article class="page page--front">
    <div class="photo front__photo" role="img" aria-label="Photo of a solar panel array beside a white power cabinet"></div>
    <div class="front__logo"><div class="brand"><span class="brand__square"></span>KAURI GRID SOLAR</div></div>
    <svg class="front__shapes" viewBox="0 0 377 140" preserveAspectRatio="none" aria-hidden="true">
      <polygon points="0,40 377,0 377,20 0,60" fill="var(--green)"/>
      <polygon points="0,60 377,20 377,140 0,140" fill="var(--paper)"/>
    </svg>
    <div class="front__title"><h1 class="h">Northland's<br>off grid technology<br>specialists</h1></div>
    <div class="front__bottom">
      <div><svg viewBox="0 0 24 24"><path d="M6.6 10.8a15 15 0 0 0 6.6 6.6l2.2-2.2a1 1 0 0 1 1-.25 11.4 11.4 0 0 0 3.6.57 1 1 0 0 1 1 1V20a1 1 0 0 1-1 1A17 17 0 0 1 3 4a1 1 0 0 1 1-1h3.5a1 1 0 0 1 1 1c0 1.25.2 2.45.57 3.57a1 1 0 0 1-.25 1z"/></svg>0800 528 474</div>
      <div><svg viewBox="0 0 24 24"><circle cx="12" cy="12" r="9"/></svg>www.kaurigridsolar.co.nz</div>
    </div>
  </article>
</section>

<section class="spread spread--inside" aria-label="Brochure inside spread">
  <article class="page page--left">
    <div class="band h" style="top:20px">The complete off grid kit</div>
    <div class="product-grid">
      <div class="product"><div class="product__img product__img--panel" role="img" aria-label="Product photo of solar panels"></div><span class="product__label">Solar Panels</span></div>
      <div class="product"><div class="product__img" role="img" aria-label="Product photo of an inverter"></div><span class="product__label">Inverter</span></div>
      <div class="product"><div class="product__img" role="img" aria-label="Product photo of a battery bank"></div><span class="product__label">Battery Bank</span></div>
      <div class="product"><div class="product__img" role="img" aria-label="Product photo of a charge controller"></div><span class="product__label">Charge Controller</span></div>
    </div>
    <div class="band h" style="top:176px">Why choose us</div>
    <div class="features" style="top:210px">
      <div class="feature"><div class="feature__title">Clean Power</div><div class="feature__text">Quiet, zero-emission energy daily.</div></div>
      <div class="feature"><div class="feature__title">Local Support</div><div class="feature__text">Northland team on call.</div></div>
      <div class="feature"><div class="feature__title">Smart Storage</div><div class="feature__text">Power through cloudy days.</div></div>
      <div class="feature"><div class="feature__title">Easy Upgrades</div><div class="feature__text">Grow your system later.</div></div>
    </div>
    <div class="features" style="top:360px">
      <div class="feature"><div class="feature__title">Fast Install</div><div class="feature__text">Running within a week.</div></div>
      <div class="feature"><div class="feature__title">Built Tough</div><div class="feature__text">Made for coastal weather.</div></div>
    </div>
  </article>

  <article class="page page--right">
    <div class="band h" style="top:20px">What's included</div>
    <div class="right__products">
      <div class="product"><div class="product__img product__img--panel" role="img" aria-label="Product photo of a panel array"></div><span class="product__label">Panel Array</span></div>
      <div class="product"><div class="product__img" role="img" aria-label="Product photo of a hybrid inverter"></div><span class="product__label">Hybrid Inverter</span></div>
      <div class="product"><div class="product__img" role="img" aria-label="Product photo of a lithium battery"></div><span class="product__label">Lithium Battery</span></div>
    </div>
    <div class="right__features">
      <div class="feature"><div class="feature__title">Monitoring</div><div class="feature__text">Track usage from anywhere.</div></div>
      <div class="feature"><div class="feature__title">Warranty</div><div class="feature__text">Long cover, full peace.</div></div>
      <div class="feature"><div class="feature__title">Backup</div><div class="feature__text">Generator ready when needed.</div></div>
    </div>
    <div class="photo install__photo" role="img" aria-label="Photo of a ground-mounted solar array in front of a rural house"></div>
  </article>
</section>

</body>
</html>
```